Tess Marlowe Communication business card

I am starting a small, country-based business that offers writing, communication and marketing services to a wide range of clients, inner city big business, to mining, through to agriculture.

The appeal of my business is that it's mobile and flexible. It's just me, with lots of hands-on experience on construction and infrastructure projects.

I can provide the following services:

• Communication planning and management
• Issues and media management
• Marketing and communication materials
• Project management and strategy
• Government liaison
• Incident management communication
• Stakeholder management

It would be great to be able to use the elements of the business card design on other stationery.

Industry/Entity Type

Communication

Requirements
Must have
• The following information:

Tess Marlowe
M: 0427 391 864
E: tess@tmcommsmail.com

PO Box 152
Durrandale Q 4472
Nice to have
• a rural element (windmill, workboots, wheat stalk)

```html
<!DOCTYPE html>
<html lang="en">
<head>
<meta charset="utf-8">
<title>Tess Marlowe Communication – Business Card</title>
<link rel="stylesheet" href="https://fonts.googleapis.com/css2?family=Bitter:wght@400;700&display=swap">
<style>
  :root {
    --backdrop: #e9e6df;
    --card-cream: #f2efdb;
    --card-shade: #e8e2c6;
    --ink-brown: #5e4c2a;
    --ink-soft: #6f5d3a;
    --sketch-tone: #a8966a;
    --sketch-pale: #d6cba6;
  }
  * { margin: 0; padding: 0; box-sizing: border-box; }
  html, body {
    width: 1200px;
    height: 800px;
    overflow: hidden;
    background: var(--backdrop);
  }
  .canvas {
    position: relative;
    width: 1200px;
    height: 800px;
  }
  .business-card {
    position: absolute;
    left: 90px;
    top: 95px;
    width: 1020px;
    height: 610px;
    background: linear-gradient(165deg, var(--card-cream) 0%, var(--card-cream) 60%, var(--card-shade) 100%);
    box-shadow: 0 6px 22px rgba(60, 45, 20, 0.18);
    overflow: hidden;
  }
  .rural-illustration {
    position: absolute;
    left: 0;
    top: 0;
    width: 1020px;
    height: 610px;
  }
  .contact-block {
    position: absolute;
    left: 72px;
    top: 178px;
    font-family: "Bitter", Georgia, serif;
    color: var(--ink-soft);
  }
  .card-name {
    font-weight: 700;
    font-size: 58px;
    line-height: 1;
    color: var(--ink-brown);
    margin-bottom: 18px;
  }
  .contact-line {
    font-weight: 400;
    font-size: 36px;
    line-height: 1.34;
  }
  .postal-address {
    font-style: normal;
    margin-top: 44px;
  }
</style>
</head>
<body>
<main class="canvas">
  <section class="business-card">
    <svg class="rural-illustration" viewBox="0 0 1020 610" role="img" aria-label="Hand-sketched brown ink windmill beside a farm shed, with open paddocks stretching across the bottom of the card">
      <defs>
        <radialGradient id="sketchTone" cx="0.78" cy="0.45" r="0.75">
          <stop offset="0" stop-color="#a8966a" stop-opacity="0.5"/>
          <stop offset="0.45" stop-color="#c2b185" stop-opacity="0.32"/>
          <stop offset="1" stop-color="#d6cba6" stop-opacity="0.12"/>
        </radialGradient>
        <filter id="softEdge" x="-10%" y="-10%" width="120%" height="120%">
          <feGaussianBlur stdDeviation="22"/>
        </filter>
      </defs>
      <path filter="url(#softEdge)" fill="url(#sketchTone)"
        d="M700 60 L800 40 L860 150 L960 230 L1000 360 L1020 430 L1020 610 L120 610 L140 570 L420 530 L610 480 L660 400 L690 300 L720 200 Z"/>
    </svg>
    <div class="contact-block">
      <h1 class="card-name">Tess Marlowe</h1>
      <p class="contact-line">0427 391 864</p>
      <p class="contact-line">tess@tmcommsmail.com</p>
      <address class="postal-address">
        <p class="contact-line">PO Box 152</p>
        <p class="contact-line">Durrandale Q 4472</p>
      </address>
    </div>
  </section>
</main>
</body>
</html>
```